Digital Marketing Website Design

I need the homepage designed for my new digital marketing agency I am starting. The main goal for this homepage is to drive people to make an appointment for me to discuss their upcoming projects. Here are some examples of the layouts that I would like to emulate.
https://www.tallorchard.com/
https://www.webmerchantry.com/
https://talewick.com/
https://drmevorran.com/
https://www.neatlynestled.org/
My main focus is to attract leads that need help with running digital ads such as Chatterbook ads and Quorix Ads. I do offer other services like SEO and other things but the main focus is digital Ads.
The final design should communicate Ember Pixelry is a Digital marketing strategist building predictable revenue for small businesses through digital ads, email and marketing automation.
Target Market(s)
30-55, business owners, income 100K+, ecommerce companies, etc.
Industry/Entity Type
Digital Marketing
Number of Pages Required
2 page
Requirements
Must have
- An appealing look and feel set to drive people to make an appointment.
There needs to be a call to action button in the far right of the navigation
The same call to action in the navigation needs to be in each section on the homepage.
I need the homepage and an about us page.

```html
<!DOCTYPE html>
<html lang="en">
<head>
<meta charset="utf-8">
<title>Ember Pixelry – Profitable Ad Campaigns for Small Businesses</title>
<link rel="stylesheet" href="https://fonts.googleapis.com/css2?family=Poppins:wght@300;400;500;600;700&display=swap">
<style>
:root{
  --accent:#e8492f;
  --ink:#111111;
  --black:#000000;
  --paper:#f8f8f8;
  --white:#ffffff;
  --muted:#8a8a8a;
  --field:#ececec;
  --logo-grey:#b9b9b9;
}
*{box-sizing:border-box;margin:0;padding:0}
html,body{width:1200px;height:2961px;overflow:hidden}
body{font-family:'Poppins',sans-serif;background:var(--paper);color:var(--ink);position:relative}
a{color:inherit;text-decoration:none}

/* header + hero */
.hero{position:absolute;left:0;top:0;width:1200px;height:620px}
.hero-blob{position:absolute;right:0;top:0}
.brand{position:absolute;left:158px;top:36px;display:flex;align-items:center;gap:8px;font-weight:700;font-size:22px;color:var(--accent);letter-spacing:.5px}
.brand-dot{width:14px;height:14px;border-radius:50%;background:var(--accent)}
.nav{position:absolute;left:685px;top:31px;display:flex;align-items:center;gap:22px;font-size:12.5px;font-weight:500;color:var(--white)}
.btn-outline-light{border:1.5px solid var(--white);padding:9px 11px;font-weight:500}
.hero-art{position:absolute;left:694px;top:100px;width:426px;height:435px;border-radius:30px;background:linear-gradient(160deg,#e9e9e9,#9a9a9a)}
.hero-copy{position:absolute;left:162px;top:242px}
.hero-kicker{font-size:31px;font-weight:400;line-height:1.2}
.hero-title{font-size:49px;font-weight:700;color:var(--accent);line-height:1.15}
.hero-lede{font-size:12px;font-weight:300;line-height:1.6;margin-top:10px;width:340px}
.hero-actions{display:flex;gap:16px;margin-top:30px}
.btn{display:inline-block;font-size:12.5px;font-weight:500;padding:12px 15px;border:1.5px solid var(--black)}
.btn-dark{background:var(--black);color:var(--white)}
.btn-light{background:transparent;color:var(--ink);padding:12px 22px}
.scroll-cue{position:absolute;left:570px;top:530px;width:60px;height:60px;border-radius:50%;background:var(--white);box-shadow:0 4px 14px rgba(0,0,0,.12);display:flex;align-items:center;justify-content:center}

/* logo band */
.logo-band{position:absolute;left:0;top:620px;width:1200px;height:98px;background:var(--black);display:flex;align-items:center;justify-content:center}
.logo-band .logos{display:flex;gap:80px;margin:0 48px}
.logo-band span{font-size:37px;font-weight:600;color:var(--logo-grey)}

/* sections */
.section-title{font-size:38px;font-weight:600;text-align:center}
.rule{width:110px;height:4px;background:var(--accent);margin:16px auto 0}
.how{position:absolute;left:0;top:762px;width:1200px}
.how p{width:850px;margin:26px auto 0;text-align:center;font-size:19.5px;line-height:1.5}
.steps-head{position:absolute;left:0;top:1113px;width:1200px}
.steps{position:absolute;top:1220px;left:0;width:1200px}
.step{position:absolute;top:0;width:262px;height:285px;background:var(--white);box-shadow:0 2px 6px rgba(0,0,0,.12);text-align:center}
.step-num{position:absolute;left:0;top:0;width:50px;height:50px;background:var(--black);color:var(--white);font-size:20px;display:flex;align-items:center;justify-content:center}
.step-icon{width:92px;height:92px;margin:10px auto 0;border-radius:8px;background:linear-gradient(135deg,#fde0da,#f6a898)}
.step p{font-size:19px;line-height:25.5px;margin:14px 8px 0}
.cta-note{position:absolute;left:175px;top:1525px;width:850px;text-align:center;font-size:19.5px;line-height:1.5}
.cta-center{position:absolute;left:486px;top:1638px;padding:14px 17px;font-size:15px}

/* testimonials */
.reviews{position:absolute;left:0;top:1779px;width:1200px;height:551px;background:var(--black);color:var(--white)}
.reviews .section-title{margin-top:22px;color:var(--white)}
.review{position:absolute;top:130px;width:277px;height:293px;background:var(--white);border-radius:26px;color:var(--ink)}
.review .q{position:absolute;font-size:60px;font-weight:700;line-height:1;font-family:Georgia,serif;font-style:italic}
.review .q-open{left:8px;top:6px}
.review .q-close{right:14px;bottom:-18px}
.review p{position:absolute;left:30px;top:42px;width:222px;font-size:15.5px;line-height:1.45}
.avatar{position:absolute;left:46px;top:262px;width:56px;height:56px;border-radius:50%;background:#555;border:5px solid var(--white)}
.reviewer{position:absolute;top:450px;width:110px;text-align:center;font-size:15px;font-weight:600}
.stars{position:absolute;top:470px;width:110px;text-align:center;color:var(--accent);font-size:14px;letter-spacing:1px}
.arrow{position:absolute}

/* newsletter */
.newsletter{position:absolute;left:0;top:2420px;width:1200px}
.newsletter h3{text-align:center;font-size:30px;font-weight:400;margin-top:18px}
.newsletter h3 strong{font-weight:600}
.subscribe{position:absolute;top:146px;left:318px;display:flex;gap:24px}
.subscribe .field{width:386px;height:48px;background:var(--field);font-size:11px;color:var(--muted);display:flex;align-items:center;padding-left:27px}
.subscribe .btn{width:153px;height:48px;display:flex;align-items:center;justify-content:center;font-size:15px}

/* footer */
.footer{position:absolute;left:0;top:2702px;width:1200px;height:259px;background:var(--black);color:var(--white)}
.footer h4{font-size:16px;font-weight:500}
.footer .col{position:absolute;top:38px}
.footer ul{list-style:none;margin-top:20px;font-size:12.5px;line-height:27px}
.footer .stay h4{font-size:24px}
.socials{display:flex;gap:22px;margin-top:24px;padding-left:10px}
.socials span{width:12px;height:12px;border-radius:50%;background:var(--white);display:block}
.contact li{display:flex;align-items:center;gap:7px}
.copyright{position:absolute;left:0;top:234px;width:1200px;text-align:center;font-size:12.5px}
</style>
</head>
<body>

<section class="hero">
  <svg class="hero-blob" width="575" height="525" viewBox="0 0 575 525" aria-hidden="true">
    <path d="M62 0 C20 40 20 100 110 150 C200 200 120 260 200 330 C280 400 360 380 430 450 C480 505 540 530 575 510 L575 0 Z" fill="#000"/>
  </svg>
  <div class="brand"><span class="brand-dot"></span>EMBER PIXELRY</div>
  <nav class="nav">
    <a href="#">Home</a><a href="#">Services</a><a href="#">About</a>
    <a href="#" class="btn-outline-light">Schedule Appointment</a>
  </nav>
  <div class="hero-art" role="img" aria-label="Illustration of a marketer stepping out of a phone with a megaphone, surrounded by email, video, camera and search icons"></div>
  <div class="hero-copy">
    <p class="hero-kicker">We Built Profitable Ad Campaigns</p>
    <h1 class="hero-title">For small businesses</h1>
    <p class="hero-lede">The selling system that brings in Predictable revenue through digital ads, email, and marketing automation.</p>
    <div class="hero-actions">
      <a href="#" class="btn btn-dark">Free Chatterbook Ads Checklist</a>
      <a href="#" class="btn btn-light">Schedule an Appointment</a>
    </div>
  </div>
  <div class="scroll-cue"><svg width="22" height="34" viewBox="0 0 22 34" aria-hidden="true"><rect x="2" y="2" width="18" height="30" rx="9" fill="none" stroke="#111" stroke-width="2"/><line x1="11" y1="8" x2="11" y2="13" stroke="#111" stroke-width="2"/></svg></div>
</section>

<section class="logo-band">
  <svg width="16" height="26" viewBox="0 0 16 26" aria-hidden="true"><path d="M13 3 L3 13 L13 23" fill="none" stroke="#fff" stroke-width="3"/></svg>
  <div class="logos"><span>(LOGO)</span><span>(LOGO)</span><span>(LOGO)</span><span>(LOGO)</span><span>(LOGO)</span></div>
  <svg width="16" height="26" viewBox="0 0 16 26" aria-hidden="true"><path d="M3 3 L13 13 L3 23" fill="none" stroke="#fff" stroke-width="3"/></svg>
</section>

<section class="how">
  <h2 class="section-title">How It Works</h2>
  <div class="rule"></div>
  <p>At Ember Pixelry Solutions we know that you want to have a profitable business. In order to do that, you need a strong system that can predictably bring in sales even in bad times. The problem is there is so much out there to wade through and so many people telling you what you should do which makes you feel frustrated, lost, and flat out stressed out. We believe that businesses with great products should get the customer. We understand the frustration which is why we are here to help you maneuver through the minutiae and create a system that flat out works.</p>
</section>

<section class="steps-head">
  <h2 class="section-title">Here’s how we do it</h2>
  <div class="rule"></div>
</section>

<section class="steps">
  <article class="step" style="left:152px">
    <div class="step-num">1</div>
    <div class="step-icon" role="img" aria-label="Icon of a consultant with documents and a gear"></div>
    <p>Schedule an appointment to go through the basics of what you need and to find out if we are a good fit to work together.</p>
  </article>
  <article class="step" style="left:450px">
    <div class="step-num">2</div>
    <div class="step-icon" role="img" aria-label="Icon of a presentation board with charts and a magnifier"></div>
    <p>Work with our team to build out your customer journey and selling system</p>
  </article>
  <article class="step" style="left:772px">
    <div class="step-num">3</div>
    <div class="step-icon" role="img" aria-label="Icon of a growing plant over stacked coins"></div>
    <p>Execute and enjoy the extra revenue!</p>
  </article>
</section>

<p class="cta-note">So, schedule your appointment today. And in the meantime, checkout our Chatterbook ads checklist. So you can stop any poor running campaigns and fill in the gaps where they are needed.</p>
<a href="#" class="btn btn-dark cta-center">Schedule an Appointment</a>

<section class="reviews">
  <h2 class="section-title">What others are saying</h2>
  <svg class="arrow" style="left:92px;top:276px" width="16" height="26" viewBox="0 0 16 26" aria-hidden="true"><path d="M13 3 L3 13 L13 23" fill="none" stroke="#fff" stroke-width="3"/></svg>
  <svg class="arrow" style="left:1092px;top:276px" width="16" height="26" viewBox="0 0 16 26" aria-hidden="true"><path d="M3 3 L13 13 L3 23" fill="none" stroke="#fff" stroke-width="3"/></svg>

  <article class="review" style="left:161px">
    <span class="q q-open">“</span>
    <p>Lorem ipsum dolor sit amet, consetetur sadipscing elitr, sed diam nonumy eirmod tempor invidunt ut labore et dolore magna aliquyam erat, sed diam voluptua. At vero eos et accusam et justo duo dolores et ea rebum. Stet clita kasd</p>
    <span class="q q-close">”</span>
    <div class="avatar" role="img" aria-label="Client portrait"></div>
  </article>
  <div class="reviewer" style="left:182px">MARCUS. T.</div><div class="stars" style="left:182px">★★★★★</div>

  <article class="review" style="left:461px">
    <span class="q q-open">“</span>
    <p>Lorem ipsum dolor sit amet, consetetur sadipscing elitr, sed diam nonumy eirmod tempor invidunt ut labore et dolore magna aliquyam erat, sed diam voluptua. At vero eos et accusam et justo duo dolores et ea rebum. Stet clita kasd</p>
    <span class="q q-close">”</span>
    <div class="avatar" role="img" aria-label="Client portrait"></div>
  </article>
  <div class="reviewer" style="left:482px">MARCUS. T.</div><div class="stars" style="left:482px">★★★★★</div>

  <article class="review" style="left:762px">
    <span class="q q-open">“</span>
    <p>Lorem ipsum dolor sit amet, consetetur sadipscing elitr, sed diam nonumy eirmod tempor invidunt ut labore et dolore magna aliquyam erat, sed diam voluptua. At vero eos et accusam et justo duo dolores et ea rebum. Stet clita kasd</p>
    <span class="q q-close">”</span>
    <div class="avatar" role="img" aria-label="Client portrait"></div>
  </article>
  <div class="reviewer" style="left:783px">MARCUS. T.</div><div class="stars" style="left:783px">★★★★★</div>
</section>

<section class="newsletter">
  <h2 class="section-title">Newsletter</h2>
  <div class="rule"></div>
  <h3>Do you want to get <strong>Special News?</strong></h3>
  <form class="subscribe">
    <div class="field">Drop Your Email</div>
    <a href="#" class="btn btn-dark">Subscribe</a>
  </form>
</section>

<footer class="footer">
  <div class="col stay" style="left:164px">
    <h4>Stay in touch</h4>
    <div class="socials"><span></span><span></span><span></span><span></span></div>
  </div>
  <div class="col" style="left:444px">
    <h4>Quick Links</h4>
    <ul><li>About</li><li>Home</li><li>Services</li><li>Appointment</li></ul>
  </div>
  <div class="col" style="left:636px">
    <h4>Legal</h4>
    <ul><li>Privacy &amp; Policy</li><li>Disclaimer</li><li>Cookies</li><li>Contact</li></ul>
  </div>
  <div class="col contact" style="left:858px">
    <h4>Contact</h4>
    <ul>
      <li><svg width="11" height="11" viewBox="0 0 12 12" aria-hidden="true"><path d="M2 1 L4.5 1 L5.5 3.8 L4 4.8 C4.8 6.5 5.6 7.3 7.2 8 L8.2 6.5 L11 7.5 L11 10 C6 11 1 6 2 1 Z" fill="#fff"/></svg>000-000-0000</li>
      <li><svg width="11" height="9" viewBox="0 0 12 9" aria-hidden="true"><rect x="0" y="0" width="12" height="9" fill="#fff"/><path d="M0 0 L6 5 L12 0" fill="none" stroke="#000" stroke-width="1.2"/></svg>hello@emberpixelry.com</li>
      <li><svg width="9" height="12" viewBox="0 0 10 13" aria-hidden="true"><path d="M5 0 C2 0 0 2 0 5 C0 8 5 13 5 13 C5 13 10 8 10 5 C10 2 8 0 5 0 Z" fill="#fff"/><circle cx="5" cy="5" r="2" fill="#000"/></svg>Fernbrook, US</li>
    </ul>
  </div>
  <p class="copyright">Copyright @ 2020 all right reserved</p>
</footer>

</body>
</html>
```